Drifting Ages Chronicle - Book Cover Design

I need a cover (front, spine, back) designed for the second edition of the historical book - Drifting Ages Chronicle. This book was created to be a more engaging supplementary resource to the dry texts of most middle and high school social studies classrooms. Although comprehensive and exhaustively researched, the book at times uses humor and irony to engage the reader. The cover should reflect this tone.

Book Title: Drifting Ages Chronicle
Subtitle: The Tales, Traditions and Turning Points of World History and the Regional Challenges of Today
Author: Noel Wickstrom
Updates

Project Deadline Extended
Reason: As multiple designers are working on adjustments and I am looking for new, creative ideas, I am extending the deadline five days. Thank you.

Project Deadline Extended
Reason: Artists are still making alterations to suggestions made and I also want to give designers a chance to submit new ideas.

Target Market(s)

Middle School and High School Teachers

Font styles to use
Serif

Colors
ec1f27
ffffff
000000

Requirements
Must have
• 1) See attachment for text for front cover, spine, back cover
• 2) Central, engaging image
Nice to have
• A subtle hint of humor, light tone
• Potentially upside down globe spinning
• Prefer black, red, white color scheme
Should not have
• Cartoonish text, images

```html
<!DOCTYPE html>
<html lang="en">
<head>
<meta charset="utf-8">
<title>Drifting Ages Chronicle – Cover Wrap</title>
<link rel="stylesheet" href="https://fonts.googleapis.com/css2?family=Tinos:ital,wght@0,400;0,700;1,400&family=PT+Sans:ital,wght@0,400;0,700;1,400&display=swap">
<style>
  :root {
    --red: #ec1f27;
    --ink: #000000;
    --paper: #f6f5f1;
    --backdrop: #e4e4e4;
    --map: #b8b5a6;
    --glass: #9a9a98;
  }
  * { box-sizing: border-box; margin: 0; padding: 0; }
  html, body { width: 1200px; height: 1200px; overflow: hidden; }
  body {
    background: var(--backdrop);
    display: flex;
    align-items: center;
    justify-content: center;
  }
  .cover-wrap {
    display: flex;
    height: 740px;
    box-shadow: 0 12px 40px rgba(0,0,0,0.18);
  }
  .panel {
    width: 500px;
    height: 100%;
    background: var(--paper);
    position: relative;
  }

  /* Back cover */
  .back-cover {
    padding: 46px 44px 40px 44px;
    font-family: "PT Sans", Arial, sans-serif;
    font-size: 14.6px;
    line-height: 1.38;
    color: var(--ink);
  }
  .back-heading { font-weight: 700; font-size: 15px; margin-bottom: 12px; }
  .back-copy p { text-align: justify; margin-bottom: 16px; }
  .back-quote { font-style: italic; text-align: justify; }
  .back-quote .attribution { font-style: normal; font-weight: 700; }

  /* Spine */
  .spine {
    width: 56px;
    height: 100%;
    background: var(--red);
    color: #fff;
    display: flex;
    flex-direction: column;
    align-items: center;
    justify-content: space-between;
    padding: 30px 0 22px;
  }
  .spine-title, .spine-credit {
    writing-mode: vertical-rl;
    font-family: "Tinos", "Times New Roman", serif;
    white-space: nowrap;
  }
  .spine-title { font-size: 25px; letter-spacing: 2px; text-transform: uppercase; }
  .spine-credit { font-size: 11px; line-height: 1.2; text-align: left; }

  /* Front cover */
  .front-cover {
    display: flex;
    flex-direction: column;
    align-items: center;
    font-family: "Tinos", "Times New Roman", serif;
    color: var(--ink);
    padding-top: 40px;
  }
  .author { font-size: 40px; font-weight: 400; }
  .cover-art { margin-top: 42px; width: 410px; height: 300px; }
  .title {
    margin-top: 28px;
    font-size: 60px;
    line-height: 1.0;
    font-weight: 400;
    color: var(--red);
    text-align: center;
  }
  .subtitle {
    position: absolute;
    bottom: 44px;
    left: 0; right: 0;
    text-align: center;
    font-size: 17.5px;
    line-height: 1.2;
  }
</style>
</head>
<body>
  <div class="cover-wrap">
    <section class="panel back-cover">
      <h2 class="back-heading">Do you know how we got to here?</h2>
      <div class="back-copy">
        <p>Well, if you’re like 97.4% of the people walking the planet, you haven’t got a clue. Sure, you might know a bit about a couple rivers in Mesopotamia, how Thessalon wandered around Athens asking questions or how Marten Lodder got ticked off one day and nailed a really long essay to the door of a church. But to be honest (and don’t be embarrassed), you’ve got some gaps. Be dense no more. In <strong><em>Drifting Ages Chronicle</em></strong>, Noel Wickstrom once again takes you through all the major tales, traditions and turning points of world history - not just European history, but WORLD history. You’ll figure out real quick that the West might have had some crowning moments, but for the whole of human history, it’s been the Persians, the Indians, the Chinese, the Muslims or some horse peoples from the steppe that have truly turned us into the clever little creatures we are today.</p>
        <p>And while most world history books fade off once the Cold War comes to a close, this sometimes sardonic tome just gets going. Updated to include contemporary debates over topics such as Brexit, the rise of ISIS, claims to the South China Sea, the mounting refugee crisis and the controversial presidency of Darnell Tromley, this second edition finishes with a distinctively comprehensive look at the 21st century challenges facing nine major regions of today’s world - Africa, Latin America, Japan, China, the Middle East, India, Russia, Europe and the United States.</p>
      </div>
      <p class="back-quote">“Noel Wickstrom expertly understands what his audience wants to know, what they need to know. A page-turning account of our proudest achievements and our most colossal bumblings. It’s world history for the rest of us.” - <span class="attribution">Idris Batawi</span></p>
    </section>

    <aside class="spine">
      <span class="spine-title">Drifting Ages Chronicle</span>
      <span class="spine-credit">Noel Wickstrom<br>Second Edition</span>
    </aside>

    <section class="panel front-cover">
      <p class="author">Noel Wickstrom</p>
      <svg class="cover-art" viewBox="0 0 410 300" role="img" aria-label="Illustration of a grey hourglass standing on a flat world map">
        <defs>
          <radialGradient id="art-tone" cx="50%" cy="45%" r="60%">
            <stop offset="0" stop-color="var(--glass)"/>
            <stop offset="1" stop-color="var(--map)"/>
          </radialGradient>
        </defs>
        <rect width="410" height="300" rx="16" fill="url(#art-tone)" opacity="0.55"/>
      </svg>
      <h1 class="title">Drifting<br>Ages Chronicle</h1>
      <p class="subtitle">The tales, traditions and turning points of world history<br>and the regional challenges of today.<br>Second Edition</p>
    </section>
  </div>
</body>
</html>
```